OKRUVI card Technical Architecture

Hello everyone OKRUVI: It is a consulting firm in Architecture and Construction. I require a card duplexing, sober, elegant, classic but not boring. Update 1: Use the following data for the card. Name: Rodrigo Salcedo Mauricio Quintana Position: COO Twitter: @okruviTB Homepage: okruvi.net home address not include the participation of all thank you.

Target Market(s)

Construction companies, Architects and Consulting Engineers

Industry/Entity Type

Consulting

Contact Information for Business Card

Los campos que debe tener:
Nombre, Cargo, email, homepage y twitter

Font styles to use
Serif
Sans Serif
Other font styles liked:
• Me gustan playfair display, open sans y roboto, pero estoy sujeto a sus propuestas

Requirements
Must have
• Colors: Present combined proposals in white, red, gray and black Update 1: The two names must be clearly differentiated from the two surnames
Nice to have
• They are free to present their best proposals. I will bring them immediate feedback to the extent you can go see their designs. Complete data for card and logo files will give the winner the

```html
<!DOCTYPE html>
<html lang="es">
<head>
<meta charset="utf-8">
<title>OKRUVI – Business Card</title>
<link href="https://fonts.googleapis.com/css2?family=Raleway:wght@400;500&family=Roboto:wght@400;500&display=swap" rel="stylesheet">
<style>
  :root {
    --backdrop: #3b3531;
    --card-black: #141414;
    --card-edge: #1d1d1d;
    --brand-red: #c4161c;
    --brand-red-deep: #8e1014;
    --silver: #c9c9c9;
    --grey-text: #8e8e8e;
    --white: #f2f2f2;
    --divider: #5a5a5a;
  }
  * { margin: 0; padding: 0; box-sizing: border-box; }
  html, body { width: 1200px; height: 864px; overflow: hidden; }
  body {
    background: var(--backdrop);
    position: relative;
    font-family: "Roboto", Arial, sans-serif;
  }
  .card {
    position: absolute;
    width: 530px;
    height: 303px;
    background: var(--card-black);
    border: 1px solid var(--card-edge);
    box-shadow: 0 14px 30px rgba(0,0,0,0.45);
  }
  /* Front */
  .card-front { left: 60px; top: 120px; }
  .front-wordmark {
    position: absolute;
    left: 0; right: 0; top: 92px;
    text-align: center;
    font-family: "Raleway", Arial, sans-serif;
    font-weight: 400;
    font-size: 50px;
    letter-spacing: 16px;
    padding-left: 16px;
    color: var(--silver);
  }
  .front-rule {
    position: absolute;
    left: 105px; right: 105px; top: 158px;
    height: 1px;
    background: var(--brand-red-deep);
  }
  .front-descriptor {
    position: absolute;
    left: 0; right: 0; top: 166px;
    text-align: center;
    font-family: "Raleway", Arial, sans-serif;
    font-size: 13px;
    letter-spacing: 5px;
    color: var(--brand-red);
    text-transform: uppercase;
  }
  .front-web {
    position: absolute;
    left: 0; right: 0; top: 222px;
    text-align: center;
    font-size: 14px;
    letter-spacing: 4px;
    color: var(--grey-text);
  }
  /* Back */
  .card-back { left: 610px; top: 440px; }
  .back-brand {
    position: absolute;
    left: 36px; top: 132px;
    width: 180px;
    text-align: center;
    font-family: "Raleway", Arial, sans-serif;
    font-size: 30px;
    font-weight: 500;
    letter-spacing: 5px;
    color: var(--brand-red);
  }
  .back-divider {
    position: absolute;
    left: 240px; top: 60px;
    width: 1px; height: 180px;
    background: var(--divider);
  }
  .contact {
    position: absolute;
    left: 262px; top: 82px;
  }
  .contact-name { font-size: 19px; color: var(--brand-red); line-height: 1.1; }
  .contact-role { font-size: 16px; color: var(--white); margin-bottom: 18px; }
  .contact-list { list-style: none; }
  .contact-item {
    display: flex; align-items: center; gap: 10px;
    font-size: 14px; color: var(--white);
    height: 22px;
  }
  .contact-icon { width: 13px; height: 13px; flex: none; }
</style>
</head>
<body>
  <section class="card card-front" aria-label="Card front">
    <div class="front-wordmark">OKRUVI</div>
    <div class="front-rule"></div>
    <div class="front-descriptor">Arquitectura Técnica</div>
    <div class="front-web">www.okruvi.net</div>
  </section>

  <section class="card card-back" aria-label="Card back">
    <div class="back-brand">OKRUVI</div>
    <div class="back-divider"></div>
    <div class="contact">
      <p class="contact-name">Mateo Lorca</p>
      <p class="contact-role">President</p>
      <ul class="contact-list">
        <li class="contact-item">
          <svg class="contact-icon" viewBox="0 0 16 16" aria-hidden="true">
            <rect x="2" y="6" width="12" height="8" rx="1.5" fill="#c4161c"/>
            <path d="M1 6 Q8 0 15 6 L12 7 Q8 4 4 7 Z" fill="#c4161c"/>
            <circle cx="8" cy="10" r="2" fill="#141414"/>
          </svg>
          <span>555 0142 7781</span>
        </li>
        <li class="contact-item">
          <svg class="contact-icon" viewBox="0 0 16 16" aria-hidden="true">
            <rect x="1" y="3" width="14" height="10" rx="1" fill="#c4161c"/>
            <path d="M1.5 3.5 L8 9 L14.5 3.5" stroke="#141414" stroke-width="1.3" fill="none"/>
          </svg>
          <span>mateo@okruvi.net</span>
        </li>
        <li class="contact-item">
          <svg class="contact-icon" viewBox="0 0 16 16" aria-hidden="true">
            <circle cx="8" cy="8" r="6" fill="#c4161c"/>
          </svg>
          <span>@okruviTB</span>
        </li>
      </ul>
    </div>
  </section>
</body>
</html>
```